Business cards for education company

We need a business card design for a relatively new company based in Queensland and operating across Australia. We resell diploma level education courses which include Business, Management, Finance, Community Services & Government courses. We offer over 20 different courses.
The target market is for anyone 16 years of age and older. There is no age limit.

We would like to see the design use the color blue and silver. The final design should communicate professionalism and a bright future.

We sell education but are also promoting the career they see themselves in 2-3 years in the future

Our company logo is attached.

Target Market(s)

We target all age groups above 16 years of age. The main target market would be people aged between 17-35.

We focus on those people who cannot make it into University or do not want to commit the time to a full degree.

Industry/Entity Type

Education

Requirements
Must have
• Professional
Company logo
website
Contact details:

Please use the following example:

Lionel Tapping
Senior Education Consultant
0417 385 960
Lionel.tapping@skylarklearninghub.com.au
www.skylarklearninghub.com.au

```html
<!DOCTYPE html>
<html lang="en">
<head>
<meta charset="utf-8">
<title>Skylark Learning Hub – Business Card</title>
<link rel="stylesheet" href="https://fonts.googleapis.com/css2?family=Open+Sans:wght@400;600;700&display=swap">
<style>
  :root {
    --canvas-bg: #e4e4e4;
    --brand-navy: #0d4a8c;
    --brand-blue: #024a8c;
    --text-blue: #0b4584;
    --silver-light: #f2f2f2;
    --silver-dark: #b9b9b9;
    --card-white: #ffffff;
    --icon-grey: #8a8a8a;
  }
  * { margin: 0; padding: 0; box-sizing: border-box; }
  html, body { width: 1200px; height: 800px; overflow: hidden; }
  body {
    position: relative;
    background: var(--canvas-bg);
    font-family: "Open Sans", Arial, sans-serif;
  }

  /* Brand lockup shown above the card */
  .brand-lockup {
    position: absolute;
    left: 70px;
    top: 108px;
    display: flex;
    align-items: center;
    gap: 22px;
  }
  .brand-dot {
    width: 86px; height: 86px;
    border-radius: 50%;
    background: var(--brand-navy);
  }
  .brand-name {
    font-size: 44px;
    font-weight: 700;
    color: var(--brand-navy);
    letter-spacing: 0.5px;
  }

  /* Business card, front */
  .business-card {
    position: absolute;
    left: 415px;
    top: 282px;
    width: 648px;
    height: 368px;
    background: var(--card-white);
    overflow: hidden;
  }
  .card-header {
    position: absolute;
    left: 0; top: 0;
    width: 100%; height: 180px;
    background: radial-gradient(ellipse 70% 120% at 52% 10%, var(--silver-light) 0%, #dcdcdc 45%, var(--silver-dark) 100%);
  }
  .card-wedge {
    position: absolute;
    left: 0; top: 0;
  }
  .card-brand {
    position: absolute;
    left: 228px;
    top: 52px;
    display: flex;
    align-items: center;
    gap: 12px;
  }
  .card-brand .brand-dot { width: 44px; height: 44px; }
  .card-brand .brand-name { font-size: 24px; }

  .holder {
    position: absolute;
    right: 19px;
    top: 121px;
    text-align: right;
    color: var(--text-blue);
  }
  .holder-name { font-size: 23px; font-weight: 600; line-height: 30px; }
  .holder-title { font-size: 20px; font-weight: 400; line-height: 28px; }

  .contact-list {
    position: absolute;
    left: 118px;
    top: 252px;
    list-style: none;
    color: var(--text-blue);
    font-size: 20px;
  }
  .contact-item {
    display: flex;
    align-items: center;
    gap: 6px;
    height: 34px;
  }
  .contact-item svg { flex: none; }
</style>
</head>
<body>

  <div class="brand-lockup">
    <span class="brand-dot"></span>
    <span class="brand-name">Skylark Learning Hub</span>
  </div>

  <section class="business-card" aria-label="Business card">
    <div class="card-header"></div>
    <svg class="card-wedge" width="648" height="368" viewBox="0 0 648 368" aria-hidden="true">
      <polygon points="0,0 193,180 0,368" fill="var(--brand-blue)"/>
    </svg>

    <div class="card-brand">
      <span class="brand-dot"></span>
      <span class="brand-name">Skylark Learning Hub</span>
    </div>

    <div class="holder">
      <p class="holder-name">Lionel Tapping</p>
      <p class="holder-title">Senior Education Consultant</p>
    </div>

    <ul class="contact-list">
      <li class="contact-item">
        <svg width="18" height="22" viewBox="0 0 18 22" aria-hidden="true">
          <rect x="4" y="1" width="10" height="20" rx="2" fill="#3a3a3a"/>
          <rect x="5.5" y="3.5" width="7" height="13" fill="#9a9a9a"/>
        </svg>
        <span>0417 385 960</span>
      </li>
      <li class="contact-item">
        <svg width="24" height="24" viewBox="0 0 24 24" aria-hidden="true">
          <circle cx="12" cy="12" r="11" fill="var(--icon-grey)"/>
          <g fill="none" stroke="#d6d6d6" stroke-width="1.2">
            <ellipse cx="12" cy="12" rx="5" ry="11"/>
            <line x1="1" y1="12" x2="23" y2="12"/>
            <line x1="12" y1="1" x2="12" y2="23"/>
            <path d="M3 6.5h18M3 17.5h18"/>
          </g>
        </svg>
        <span>www.skylarklearninghub.com.au</span>
      </li>
      <li class="contact-item">
        <svg width="26" height="20" viewBox="0 0 26 20" aria-hidden="true">
          <rect x="1" y="2" width="24" height="16" fill="#f4f4f4" stroke="var(--icon-grey)" stroke-width="1.4"/>
          <path d="M1 2l12 9 12-9M1 18l9-8M25 18l-9-8" fill="none" stroke="var(--icon-grey)" stroke-width="1.2"/>
        </svg>
        <span>Lionel.tapping@skylarklearninghub.com.au</span>
      </li>
    </ul>
  </section>

</body>
</html>
```